Etiketten für Honig und Honigerzeugnisse.
Vielen Dank für die gute Zusammenarbeit. Unsere Wünsche wurden prompt und zu unserer vollsten Zufriedenheit umgesetzt. Wir würden jederzeit wieder einen Auftrag an Sie vergeben. Imkerei M.Quandtberg
Zielgruppe
Wir sind eine recht junge Imkerei, welche regionale Produkte rund um die Biene anbietet.
Unsere Zielgruppe sind junge Menschen/Familien und Kunden, welche die regionalität eine Produktes über den Preis stellen.
Aufgabenstellung
Wir verwenden 2 verschiedene Gläsergrößen (250g und 500g) mit dementsprechend unterschiedlichen Etikettengrößen (42mm x 120mm sowie 55mm x 150mm).
Des weiteren benutzen wir das Siegeletikett des Netzwerkes "Goldene Wiesenkette" (http://goldene-wiesenkette.de/gwk/gwk.imker/index.html). Dieses sollte zum Desing der Etiketten passen.
Folgende Honige werden produziert:
- Frühjahrsblütenhonig,
- Sommerblütenhonig,
- Phaceliahonig,
- Sonnenblumenhonig,
- Akazienhonig,
- Buchweizenhonig,
- Heidehonig,
- Blütenhonig.
Außerdem werden noch spezielle Gewürz-Honigmischungen hergestellt:
- Aronia in Honig, Zutaten: Frühjahrsblütenhonig, Bio-Aroniapulver
- Zimt in Honig, Zutaten: Frühjahrsblütenhonig, Bio-Ceylon-Zimt
- Vanille in Honig, Zutaten: Frühjahrsblütenhonig, Bourbon-Vanillemark
- Ingwer in Honig, Zutaten: Frühjahrsblütenhonig, Bio-Ingwer
Was auf dem Etikett vorhanden sein muss:
- Deutscher Honig
- Honigsorte
- Inhalt (250g bzw 500g)
- Mehrwegglas, zurück zum Imker
- mindestens haltbar bis:
- Trocken, vor Wärme und Licht geschützt lagern.
- Imkerei M.Quandtberg, Kiefernsteig 7, 02694 Lindenhain

```html
<!DOCTYPE html>
<html lang="de">
<head>
<meta charset="utf-8">
<title>Honigetiketten – Imkerei M. Quandtberg</title>
<link rel="stylesheet" href="https://fonts.googleapis.com/css2?family=Amatic+SC:wght@700&family=Ubuntu:wght@400;500&display=swap">
<style>
  :root {
    --page: #ececec;
    --label: #2e2e2e;
    --spring-green: #c6d993;
    --white: #ffffff;
    --ink: #2e2e2e;
  }
  * { box-sizing: border-box; margin: 0; padding: 0; }
  html, body { width: 1200px; height: 1200px; overflow: hidden; }
  body {
    background: var(--page);
    font-family: "Ubuntu", Arial, sans-serif;
    position: relative;
  }
  .label {
    position: absolute;
    background: var(--label);
    color: var(--white);
    box-shadow: 0 1px 3px rgba(0,0,0,.25);
  }
  .label--250 { width: 408px; height: 144px; --u: 1px; }
  .label--500 { width: 511px; height: 186px; --u: 1.27px; }
  .label--spring { --accent: var(--spring-green); }
  .label--aronia { --accent: var(--white); }

  .storage-note, .ingredients {
    position: absolute;
    left: calc(var(--u) * 12);
    font-size: calc(var(--u) * 8.2);
    line-height: 1.3;
  }
  .storage-note { top: calc(var(--u) * 14); }
  .label--aronia .ingredients { top: calc(var(--u) * 11); }
  .label--aronia .storage-note { top: calc(var(--u) * 66); }
  .ingredients span { display: block; margin-bottom: calc(var(--u) * 3); }

  .net-weight {
    position: absolute;
    left: calc(var(--u) * 12);
    top: calc(var(--u) * 107);
    font-size: calc(var(--u) * 16);
  }

  .brand-panel {
    position: absolute;
    left: calc(var(--u) * 166);
    top: 0;
    width: calc(var(--u) * 79);
    height: calc(var(--u) * 79);
    background: var(--accent);
    color: var(--ink);
    display: flex;
    flex-direction: column;
    align-items: center;
    justify-content: flex-end;
    padding-bottom: calc(var(--u) * 7);
  }
  .brand-name {
    font-size: calc(var(--u) * 8.5);
    font-weight: 500;
    display: flex;
    align-items: center;
    gap: calc(var(--u) * 3);
    margin-bottom: calc(var(--u) * 14);
  }
  .brand-name::before {
    content: "";
    width: calc(var(--u) * 7);
    height: calc(var(--u) * 7);
    background: var(--ink);
  }
  .origin-mark { font-size: calc(var(--u) * 8); }

  .variety {
    position: absolute;
    left: calc(var(--u) * 80);
    width: calc(var(--u) * 248);
    top: calc(var(--u) * 84);
    text-align: center;
    font-family: "Amatic SC", "Arial Narrow", sans-serif;
    font-weight: 700;
    font-size: calc(var(--u) * 24);
    line-height: 1;
    text-transform: uppercase;
    color: var(--accent);
    letter-spacing: .01em;
  }

  .region-tag {
    position: absolute;
    left: calc(var(--u) * 166);
    top: calc(var(--u) * 118);
    width: calc(var(--u) * 79);
    height: calc(var(--u) * 26);
    background: var(--accent);
    color: var(--ink);
    font-size: calc(var(--u) * 8);
    display: flex;
    align-items: center;
    justify-content: center;
  }

  .producer, .return-note, .best-before {
    position: absolute;
    right: calc(var(--u) * 10);
    text-align: right;
    font-size: calc(var(--u) * 8.2);
    line-height: 1.3;
  }
  .producer { top: calc(var(--u) * 12); }
  .return-note { top: calc(var(--u) * 66); }
  .best-before { top: calc(var(--u) * 98); }
  .best-before-field {
    display: block;
    margin-top: calc(var(--u) * 4);
    margin-left: auto;
    width: calc(var(--u) * 90);
    height: calc(var(--u) * 19);
    background: var(--white);
  }
</style>
</head>
<body>

  <article class="label label--250 label--spring" style="left:396px; top:131px;">
    <p class="storage-note">Trocken, vor Wärme und<br>Licht geschützt lagern.</p>
    <p class="net-weight">250g</p>
    <div class="brand-panel">
      <span class="brand-name">M.Quandtberg</span>
      <span class="origin-mark">Deutscher Honig</span>
    </div>
    <h2 class="variety">Frühjahrsblütenhonig</h2>
    <div class="region-tag">aus der Region</div>
    <p class="producer">Imkerei<br>M. Quandtberg<br>Kiefernsteig 7<br>02694 Lindenhain</p>
    <p class="return-note">MEHRWEGGLAS<br>Bitte zurück zum Imker</p>
    <div class="best-before">mindestens haltbar bis:<span class="best-before-field"></span></div>
  </article>

  <article class="label label--500 label--spring" style="left:346px; top:346px;">
    <p class="storage-note">Trocken, vor Wärme und<br>Licht geschützt lagern.</p>
    <p class="net-weight">500g</p>
    <div class="brand-panel">
      <span class="brand-name">M.Quandtberg</span>
      <span class="origin-mark">Deutscher Honig</span>
    </div>
    <h2 class="variety">Frühjahrsblütenhonig</h2>
    <div class="region-tag">aus der Region</div>
    <p class="producer">Imkerei<br>M. Quandtberg<br>Kiefernsteig 7<br>02694 Lindenhain</p>
    <p class="return-note">MEHRWEGGLAS<br>Bitte zurück zum Imker</p>
    <div class="best-before">mindestens haltbar bis:<span class="best-before-field"></span></div>
  </article>

  <article class="label label--250 label--aronia" style="left:396px; top:684px;">
    <p class="ingredients"><span>Zutaten:</span>Frühjahrsblütenhonig,<br>Bio-Aroniapulver</p>
    <p class="storage-note">Trocken, vor Wärme und<br>Licht geschützt lagern.</p>
    <p class="net-weight">250g</p>
    <div class="brand-panel">
      <span class="brand-name">M.Quandtberg</span>
      <span class="origin-mark">Deutscher Honig</span>
    </div>
    <h2 class="variety">Aronia in Honig</h2>
    <div class="region-tag">aus der Region</div>
    <p class="producer">Imkerei<br>M. Quandtberg<br>Kiefernsteig 7<br>02694 Lindenhain</p>
    <p class="return-note">MEHRWEGGLAS<br>Bitte zurück zum Imker</p>
    <div class="best-before">mindestens haltbar bis:<span class="best-before-field"></span></div>
  </article>

  <article class="label label--500 label--aronia" style="left:344px; top:882px;">
    <p class="ingredients"><span>Zutaten:</span>Frühjahrsblütenhonig,<br>Bio-Aroniapulver</p>
    <p class="storage-note">Trocken, vor Wärme und<br>Licht geschützt lagern.</p>
    <p class="net-weight">500g</p>
    <div class="brand-panel">
      <span class="brand-name">M.Quandtberg</span>
      <span class="origin-mark">Deutscher Honig</span>
    </div>
    <h2 class="variety">Aronia in Honig</h2>
    <div class="region-tag">aus der Region</div>
    <p class="producer">Imkerei<br>M. Quandtberg<br>Kiefernsteig 7<br>02694 Lindenhain</p>
    <p class="return-note">MEHRWEGGLAS<br>Bitte zurück zum Imker</p>
    <div class="best-before">mindestens haltbar bis:<span class="best-before-field"></span></div>
  </article>

</body>
</html>
```